Primary Home Page Graphic: Crowdfund and Non-Profit Social Promotion Website

WHAT WE NEED: See attached. I need a graphic designed that is comparable to these. The graphic will replace the home page video on our current website Quenvale.com
PREFERRED LOOK: Much like attached. Black/white with color that pops. Must have crowdfunding/non-profit + social media appearance.
WHAT WE DO: Social Promotion of Crowdfunding and Non-Profit Campaigns > the image you design should reflect this subject content.
TEXT ON GRAPHIC:
Your Campaign, Shared.
Get your message moving across social media within minutes.
Thousands of social voices are on stand-by and ready to assist.
Project Deadline Extended
Reason: Not seeing the perfect fit yet for the page. Want to see if we can get some other ideas. Looking for black and white image with title and text displayed in a modern way.
The main graphic needs to appear such as Crowdfunding. Keep the text the same with a call to action.
Please use close attention to detail, modern design technique and good contrast on the colors. Thanks.
Non Profit

```html
<!DOCTYPE html>
<html lang="en">
<head>
<meta charset="utf-8">
<title>Your Campaign, Shared</title>
<link rel="stylesheet" href="https://fonts.googleapis.com/css2?family=Open+Sans:wght@400;600;700;800&display=swap">
<style>
  :root {
    --bg-dark: #0b0b0b;
    --bg-mid: #1c1c1c;
    --tile: #ffffff;
    --icon: #3a3a3a;
    --map-light: #4a4a4a;
    --map-dark: #262626;
    --accent: #ff5a2c;
    --accent-dark: #e0461b;
    --text-main: #ffffff;
    --text-soft: #c9c9c9;
  }
  * { margin: 0; padding: 0; box-sizing: border-box; }
  html, body { width: 1200px; height: 534px; overflow: hidden; }
  body {
    font-family: "Open Sans", sans-serif;
    background: var(--bg-dark);
  }
  .hero {
    position: relative;
    width: 1200px;
    height: 534px;
    overflow: hidden;
    background: linear-gradient(180deg, var(--bg-mid) 0%, var(--bg-dark) 100%);
  }
  .world-map {
    position: absolute;
    left: 20px; top: 60px;
    width: 560px; height: 420px;
    border-radius: 40% 50% 45% 40%;
    background: radial-gradient(ellipse at 45% 45%, var(--map-light) 0%, var(--map-dark) 55%, transparent 75%);
    opacity: .8;
  }

  .hero-copy {
    position: absolute;
    left: 44px; top: 96px;
    width: 490px;
    color: var(--text-main);
  }
  .hero-copy__rule {
    width: 56px; height: 5px;
    background: var(--accent);
    margin-bottom: 18px;
  }
  .hero-copy__title {
    font-size: 46px;
    font-weight: 800;
    line-height: 1.1;
    letter-spacing: -0.5px;
    margin-bottom: 18px;
  }
  .hero-copy__title span { color: var(--accent); }
  .hero-copy__lead {
    font-size: 19px;
    font-weight: 600;
    line-height: 1.4;
    margin-bottom: 8px;
  }
  .hero-copy__note {
    font-size: 15px;
    font-weight: 400;
    line-height: 1.5;
    color: var(--text-soft);
    margin-bottom: 26px;
  }
  .hero-copy__cta {
    display: inline-block;
    padding: 13px 28px;
    background: var(--accent);
    border-bottom: 3px solid var(--accent-dark);
    color: var(--text-main);
    font-size: 15px;
    font-weight: 700;
    letter-spacing: 1px;
    text-transform: uppercase;
    text-decoration: none;
  }

  .tile {
    position: absolute;
    background: var(--tile);
  }
  .tile-photo { position: absolute; }
  .tile-badge {
    position: absolute;
    background: var(--tile);
    display: flex; align-items: center; justify-content: center;
  }
  .tile-badge svg, .icon-tile svg { fill: var(--icon); }
  .tile--feature { left: 571px; top: 7px; width: 581px; height: 232px; }
  .tile--feature .tile-photo {
    left: 25px; top: 23px; width: 532px; height: 186px;
    background: linear-gradient(180deg, #1e1e1e 0%, #3b3b3b 50%, #141414 100%);
  }
  .tile--feature .tile-badge { left: 502px; top: 153px; width: 55px; height: 56px; }

  .tile--portrait { left: 571px; top: 251px; width: 285px; height: 176px; }
  .tile--portrait .tile-photo {
    left: 13px; top: 12px; width: 260px; height: 152px;
    background: linear-gradient(90deg, #ececec 0%, #d4d4d4 45%, #5a5a5a 72%, #8a8a8a 85%, #d8d8d8 100%);
  }
  .tile--portrait .tile-badge { left: 221px; top: 114px; width: 52px; height: 50px; }

  .tile--street { left: 868px; top: 251px; width: 284px; height: 176px; }
  .tile--street .tile-photo {
    left: 12px; top: 12px; width: 260px; height: 152px;
    background: linear-gradient(180deg, #8e8e8e 0%, #6a6a6a 40%, #a8a8a8 70%, #4a4a4a 100%);
  }
  .tile--street .tile-badge { left: 220px; top: 114px; width: 52px; height: 50px; }

  .icon-tile {
    position: absolute; top: 438px; width: 87px; height: 86px;
    background: var(--tile);
    display: flex; align-items: center; justify-content: center;
  }
  .icon-tile--location { left: 571px; }
  .icon-tile--location svg { fill: var(--accent); }
  .icon-tile--feed { left: 672px; }
  .icon-tile--quote { left: 769px; }
  .icon-tile--attach { left: 868px; }

  .menu-button {
    position: absolute; left: 17px; top: 440px; width: 80px; height: 81px;
    background: var(--tile);
    display: flex; align-items: center; justify-content: center;
  }
  .menu-button svg { fill: #111; }
</style>
</head>
<body>
<main class="hero">
  <div class="world-map" role="img" aria-label="World map with glowing connection arcs linking cities across the Americas"></div>

  <header class="hero-copy">
    <div class="hero-copy__rule"></div>
    <h1 class="hero-copy__title">Your Campaign, <span>Shared.</span></h1>
    <p class="hero-copy__lead">Get your message moving across social media within minutes.</p>
    <p class="hero-copy__note">Thousands of social voices are on stand-by and ready to assist.</p>
    <a class="hero-copy__cta" href="#start">Share My Campaign</a>
  </header>

  <section class="tile tile--feature">
    <div class="tile-photo" role="img" aria-label="Photo of wooden letters spelling ME on a dark wood surface"></div>
    <div class="tile-badge">
      <svg width="28" height="26" viewBox="0 0 28 26"><path d="M2 2h24v16H2z M5 5v10h18V5z" fill-rule="evenodd"/><rect x="9" y="20" width="10" height="3"/></svg>
    </div>
  </section>

  <section class="tile tile--portrait">
    <div class="tile-photo" role="img" aria-label="Photo of a smiling woman with long dark hair"></div>
    <div class="tile-badge">
      <svg width="24" height="16" viewBox="0 0 24 16"><rect x="0" y="2" width="16" height="12" rx="1"/><path d="M16 6l8-5v14l-8-5z"/></svg>
    </div>
  </section>

  <section class="tile tile--street">
    <div class="tile-photo" role="img" aria-label="Photo of a vintage car parked in front of a roadside diner"></div>
    <div class="tile-badge">
      <svg width="24" height="22" viewBox="0 0 24 22"><path d="M0 0h24v22H0z M3 3v16h18V3z" fill-rule="evenodd"/><path d="M5 17l5-7 4 5 2-3 4 5z"/><circle cx="16" cy="7" r="2"/></svg>
    </div>
  </section>

  <div class="icon-tile icon-tile--location">
    <svg width="34" height="52" viewBox="0 0 34 52"><path d="M17 0C7.6 0 0 7.6 0 17c0 12 17 35 17 35s17-23 17-35C34 7.6 26.4 0 17 0zm0 24a7 7 0 1 1 0-14 7 7 0 0 1 0 14z"/></svg>
  </div>
  <div class="icon-tile icon-tile--feed">
    <svg width="48" height="48" viewBox="0 0 48 48"><circle cx="7" cy="41" r="7"/><path d="M0 16v9a23 23 0 0 1 23 23h9A32 32 0 0 0 0 16z"/><path d="M0 0v9a39 39 0 0 1 39 39h9A48 48 0 0 0 0 0z"/></svg>
  </div>
  <div class="icon-tile icon-tile--quote">
    <svg width="50" height="38" viewBox="0 0 50 38"><path d="M22 0C9 4 0 13 0 25a12 12 0 1 0 12-12c0-5 4-9 10-11z"/><path d="M50 0C37 4 28 13 28 25a12 12 0 1 0 12-12c0-5 4-9 10-11z"/></svg>
  </div>
  <div class="icon-tile icon-tile--attach">
    <svg width="46" height="52" viewBox="0 0 46 52"><path d="M38 20L18 40a7 7 0 0 1-10-10L30 8a4.5 4.5 0 0 1 6.4 6.4L16 35" fill="none" stroke="#3a3a3a" stroke-width="4" stroke-linecap="round"/></svg>
  </div>

  <div class="menu-button">
    <svg width="26" height="26" viewBox="0 0 26 26"><rect x="0" y="0" width="11" height="11"/><rect x="15" y="0" width="11" height="11"/><rect x="0" y="15" width="11" height="11"/><rect x="15" y="15" width="11" height="11"/></svg>
  </div>
</main>
</body>
</html>
```